8 1/2 x 11 Flyer Design for Water Damage Restoration Company

Houston Texas based Water Damage Restoration company is needing a advertising flyer that highlights water damage and water extraction.

KESTRAL Emergency Services
25810 Lindgrove Parkway Suite C4
Houston, Texas 77391
713-555-0187
www.KESTRAL81902.example

Water Damage Restoration
Water Extraction
Mold Prevention
24/7/365
FREE Evaluations

Suggested photos to use:
Water Damage
Leaking Pipes
Water on floors and ground
Water pouring from ceilings
Technicians
Company Logo
Photos

Company Colors:
Orange and Blue

```html
<!DOCTYPE html>
<html lang="en">
<head>
<meta charset="utf-8">
<title>KESTRAL Emergency Services – Water Damage Restoration Flyer</title>
<link rel="stylesheet" href="https://fonts.googleapis.com/css2?family=Montserrat:wght@500;600;700;800;900&family=Poppins:wght@500;600;700&display=swap">
<style>
:root{
  --navy:#1d3a6b;
  --navy-deep:#1a3461;
  --orange:#f26a1b;
  --sky:#3f9cf2;
  --sky-pale:#e6f2fd;
  --ink:#2b2b2b;
  --charcoal:#3b3c3f;
  --paper:#ffffff;
  --backdrop:#ececee;
}
*{margin:0;padding:0;box-sizing:border-box}
html,body{width:1200px;height:2754px;overflow:hidden;background:var(--backdrop)}
body{position:relative;font-family:"Montserrat",Arial,sans-serif}
.flyer{
  position:absolute;left:50px;top:665px;width:928px;height:1203px;
  transform:scale(1.1853);transform-origin:top left;
  background:var(--paper);overflow:hidden;
  box-shadow:0 10px 30px rgba(0,0,0,.18);
}
.abs{position:absolute}
.hero-photo{position:absolute;left:450px;top:-120px;width:600px;height:600px}
.brand{left:39px;top:58px;color:var(--navy);font-weight:800;line-height:1}
.brand .name{font-size:82px;letter-spacing:1px}
.brand .sub{font-size:24px;margin-top:6px;letter-spacing:.5px}
.headline{left:38px;top:206px;color:var(--navy);font-weight:900;font-size:50px;line-height:.92;letter-spacing:.5px}
.subhead{left:37px;top:314px;color:var(--ink);font-family:"Poppins",sans-serif;font-weight:600;font-size:21px;line-height:1.2}
.tagline{left:62px;top:390px;color:var(--orange);font-weight:800;font-size:24.5px;line-height:1.2}
.tagline-bar{left:38px;top:394px;width:3px;height:50px;background:var(--navy)}
.services-band{left:0;top:478px;width:928px;height:372px;
  background:linear-gradient(180deg,#fff 0%,var(--sky-pale) 8%,var(--sky) 35%,var(--sky) 60%,var(--sky-pale) 88%,#fff 100%)}
.wave{left:0;width:928px;height:40px}
.services-frame{left:118px;top:520px;width:686px;height:286px;border:2.5px solid var(--orange);border-radius:6px}
.services-title{left:140px;top:503px;padding:0 10px;background:#f5f9fe;color:var(--navy);font-family:"Poppins",sans-serif;font-weight:700;font-size:25px;white-space:nowrap}
.card{width:303px;height:246px;border:3px solid var(--navy);border-radius:8px;overflow:hidden;background:var(--navy)}
.card .photo{height:183px}
.card .label{height:60px;color:#fff;font-family:"Poppins",sans-serif;font-weight:600;font-size:26px;display:flex;align-items:center;justify-content:center}
.stat{color:var(--orange);font-weight:900;font-size:40px;line-height:1}
.stat-unit{color:var(--navy);font-weight:800;font-size:24px;line-height:1}
.stat-caption{left:38px;top:942px;color:var(--ink);font-family:"Poppins",sans-serif;font-weight:600;font-size:19.5px}
.evaluations{left:0;top:980px;width:352px;height:48px;background:var(--orange);clip-path:polygon(0 0,100% 0,calc(100% - 14px) 100%,0 100%);color:#fff;font-weight:900;font-size:28px;padding-left:37px;line-height:48px;letter-spacing:.5px}
.footer-dark{left:0;top:1060px;width:440px;height:143px;background:var(--charcoal)}
.footer-navy{left:400px;top:1030px;width:528px;height:173px;background:var(--navy);clip-path:polygon(60px 0,100% 0,100% 100%,0 100%)}
.phone-strip{left:450px;top:1062px;width:478px;height:62px;background:#fff;clip-path:polygon(20px 0,100% 0,100% 100%,0 100%)}
.phone{left:473px;top:1064px;color:var(--navy);font-weight:900;font-size:46px;display:flex;align-items:center;gap:14px;letter-spacing:1px}
.web{left:520px;top:1134px;color:#fff;font-weight:700;font-size:20px;display:flex;align-items:center;gap:10px;letter-spacing:.5px}
.company{left:37px;top:1082px;color:#fff;font-family:"Poppins",sans-serif;font-weight:600;font-size:15px}
.company b{color:var(--orange);font-weight:600}
.address{left:37px;top:1118px;color:#fff;font-family:"Poppins",sans-serif;font-weight:600;font-size:15px;line-height:1.15;display:flex;gap:14px;align-items:center}
.van{left:395px;top:870px;width:440px;height:190px}
</style>
</head>
<body>
<main class="flyer">
  <svg class="hero-photo" viewBox="0 0 600 600" role="img" aria-label="Photo of a technician in blue overalls repairing pipes under a kitchen sink">
    <defs>
      <linearGradient id="heroFill" x1="0" y1="0" x2="1" y2="1">
        <stop offset="0" stop-color="#d9d6d2"/><stop offset=".5" stop-color="#8a8580"/><stop offset="1" stop-color="#2f52a8"/>
      </linearGradient>
    </defs>
    <circle cx="440" cy="310" r="312" fill="var(--orange)"/>
    <circle cx="446" cy="296" r="300" fill="url(#heroFill)"/>
  </svg>

  <div class="abs brand"><div class="name">KESTRAL</div><div class="sub">EMERGENCY SERVICES</div></div>
  <h1 class="abs headline">WATER DAMAGE<br>RESTORATION</h1>
  <p class="abs subhead">Fast &amp; Reliable Residential And<br>Commercial Services</p>
  <div class="abs tagline-bar"></div>
  <p class="abs tagline">GETTING YOUR LIFE BACK TO<br>NORMAL WITH PROFESSIONAL SERVICES</p>

  <section class="abs services-band"></section>
  <svg class="abs wave" style="top:462px" viewBox="0 0 928 40" aria-hidden="true">
    <path d="M0 22 Q60 8 120 22 T240 22 T360 20 T480 22 T600 20 T720 22 T840 20 T928 22" stroke="#2c78c9" stroke-width="6" fill="none"/>
    <path d="M0 26 Q70 16 140 26 T280 26 T420 24 T560 26 T700 24 T840 26 T928 24" stroke="#9fcdf5" stroke-width="3" fill="none"/>
  </svg>
  <svg class="abs wave" style="top:828px" viewBox="0 0 928 40" aria-hidden="true">
    <path d="M0 20 Q60 8 120 20 T240 20 T360 18 T480 20 T600 18 T720 20 T840 18 T928 20" stroke="#2c78c9" stroke-width="6" fill="none"/>
    <path d="M0 24 Q70 14 140 24 T280 24 T420 22 T560 24 T700 22 T840 24 T928 22" stroke="#9fcdf5" stroke-width="3" fill="none"/>
  </svg>

  <div class="abs services-frame"></div>
  <h2 class="abs services-title">Houston Water Damage Restoration Services</h2>
  <article class="abs card" style="left:150px;top:545px">
    <div class="photo" role="img" aria-label="Photo of a technician in protective suit spraying a room" style="background:linear-gradient(135deg,#f1f1f1,#cfd3d6)"></div>
    <div class="label">Water Extraction</div>
  </article>
  <article class="abs card" style="left:470px;top:545px">
    <div class="photo" role="img" aria-label="Photo of a water treatment tank with murky brown water" style="background:linear-gradient(160deg,#c9c7c2,#6e5140 70%,#4a3426)"></div>
    <div class="label">Mold Prevention</div>
  </article>

  <div class="abs" style="left:38px;top:866px"><div class="stat">24|7</div><div class="stat-unit">HOUR</div></div>
  <svg class="abs" style="left:166px;top:866px" width="64" height="64" viewBox="0 0 64 64" aria-hidden="true">
    <path d="M10 30 A22 22 0 0 1 50 18" stroke="var(--orange)" stroke-width="4" fill="none"/>
    <path d="M54 34 A22 22 0 0 1 14 46" stroke="var(--orange)" stroke-width="4" fill="none"/>
    <path d="M44 12 L52 18 L44 22" stroke="var(--orange)" stroke-width="4" fill="none"/>
    <path d="M20 52 L12 46 L20 42" stroke="var(--orange)" stroke-width="4" fill="none"/>
    <circle cx="32" cy="32" r="11" stroke="var(--orange)" stroke-width="3" fill="none"/>
    <path d="M32 25 V32 L37 35" stroke="var(--orange)" stroke-width="3" fill="none"/>
  </svg>
  <div class="abs" style="left:262px;top:866px;text-align:right"><div class="stat">365</div><div class="stat-unit">DAYS</div></div>
  <p class="abs stat-caption">Damage Restoration Services</p>
  <div class="abs evaluations">FREE EVALUATIONS</div>

  <div class="abs footer-dark"></div>
  <div class="abs footer-navy"></div>
  <div class="abs phone-strip"></div>
  <p class="abs company"><b>KESTRAL</b> Emergency Services</p>
  <div class="abs address">
    <svg width="18" height="24" viewBox="0 0 18 24" aria-hidden="true"><path d="M9 1 C4 1 1 5 1 9 C1 15 9 23 9 23 C9 23 17 15 17 9 C17 5 14 1 9 1 Z" fill="#fff"/><circle cx="9" cy="9" r="3.5" fill="var(--charcoal)"/></svg>
    <span>25810 Lindgrove Parkway Suite C4<br>Houston, Texas 77391</span>
  </div>
  <div class="abs phone">
    <svg width="34" height="34" viewBox="0 0 24 24" aria-hidden="true"><path d="M6.6 10.8a15 15 0 0 0 6.6 6.6l2.2-2.2a1 1 0 0 1 1-.25 11.4 11.4 0 0 0 3.6.57 1 1 0 0 1 1 1V20a1 1 0 0 1-1 1A17 17 0 0 1 3 4a1 1 0 0 1 1-1h3.5a1 1 0 0 1 1 1c0 1.25.2 2.45.57 3.57a1 1 0 0 1-.25 1z" fill="var(--orange)"/></svg>
    713-555-0187
  </div>
  <div class="abs web">
    <svg width="18" height="18" viewBox="0 0 20 20" aria-hidden="true"><circle cx="10" cy="10" r="8.5" stroke="var(--orange)" stroke-width="2" fill="none"/><path d="M1.5 10h17M10 1.5c-4 4-4 13 0 17M10 1.5c4 4 4 13 0 17" stroke="var(--orange)" stroke-width="1.6" fill="none"/></svg>
    www.KESTRAL81902.example
  </div>

  <div class="abs van" role="img" aria-label="Photo of the company's orange and blue branded service van" style="background:linear-gradient(180deg,#f06a22 0%,#f06a22 45%,#dfe8f2 62%,#2a4f8f 100%);border-radius:40px 60px 24px 24px"></div>
</main>
</body>
</html>
```